Merrivale construction website for a high end luxury custom home builder

I need a website designed for a high end luxury custom home builder. I would like the website to host a number activities. A blog/vlog on the page where I can post about the projects being built how to's what to look out for during the build, A designated testimonial page but also having testimonials posted on the other pages like the gallery linked to the photos of the completed projects. a gallery page, an about us page, services page that demonstrate what we do and what we are capable of, and hopefully when I start winning awards, and awards page.
Home page
about us page
services page
gallery
testimonial
awards page but I my need to add that later.
I already have the domain name for the website. www.merrivaleconstruction.com.au
I recently completed a sketch hive page for my logo and will post the logo documents below.

Target Market(s)

I'd like to target professions with cash enough to build a house. I would like peolpe to understand that they are buy a price when they are getting quote to build there house. It seems like people just look for the cheapest price and end up with an inferior product. Where as people need to understand that a builder with the high price ( not astronomically higher 15-20% higher) are the ones with correct systems in place, a bide by correct OHS and use proper and correct product. If that can be conveyed through the website somehow, without saying it directly, it would be awesome.

Font styles to use
Sans Serif

Requirements
Must have
• I would like the testimonials to have a designated page (mentioned in the brief) but I would like the testimonials to be linked to the gallery page and when the picture are open of completed job the relevant testimonials would pop up near the pictures.

Nice to have
• I would like peolpe to understand that they are buy a price when they are getting quote to build there house. It seems like people just look for the cheapest price and end up with an inferior product. Where as people need to understand that a builder with the high price ( not astronomically higher 15-20% higher) are the ones with correct systems in place, a bide by correct OHS and use proper and correct product. If that can be conveyed through the website somehow, without saying it directly, it would be awesome.

```html
<!DOCTYPE html>
<html lang="en">
<head>
<meta charset="utf-8">
<title>Merrivale Construction — Custom Home Builder</title>
<link href="https://fonts.googleapis.com/css2?family=Cinzel:wght@400;600;700&family=Lato:wght@400;700&display=swap" rel="stylesheet">
<style>
:root{
  --blue:#1b6fc0;
  --blue-deep:#1e6cb5;
  --footer-blue:#2573b9;
  --ink:#3d3d3d;
  --body:#5b5b5b;
  --grey-bar:#4a4a4a;
  --nav:#555555;
  --line:#bfbfbf;
  --white:#ffffff;
}
*{margin:0;padding:0;box-sizing:border-box}
html,body{width:1200px;height:3486px;overflow:hidden;background:var(--white)}
body{position:relative;font-family:"Lato",sans-serif;color:var(--body)}
.abs{position:absolute}
a{color:inherit;text-decoration:none}
.heading{font-family:"Cinzel",serif;font-weight:600;color:var(--ink);letter-spacing:1px}
.rule{position:absolute;height:2px;background:linear-gradient(90deg,transparent,#666 50%,transparent)}
.btn-outline{position:absolute;border:2px solid var(--blue);border-radius:20px;color:var(--ink);font-size:12px;display:flex;align-items:center;justify-content:center;background:var(--white)}

/* header */
.call{left:75px;top:22px;display:flex;align-items:center;gap:6px}
.call-icon{width:32px;height:32px;border-radius:50%;background:var(--blue);display:flex;align-items:center;justify-content:center}
.call-text{font-size:11px;line-height:14px;color:#333}
.call-text span{color:#888}
.brand{left:520px;top:18px;display:flex;align-items:center;gap:8px}
.brand-mark{width:30px;height:30px;border-radius:50%;background:var(--blue)}
.brand-name{font-family:"Cinzel",serif;font-weight:700;color:var(--blue);font-size:17px;line-height:18px;width:130px}
.quote-btn{left:1006px;top:21px;width:118px;height:32px;border-radius:16px;background:var(--blue);color:var(--white);font-size:12px;display:flex;align-items:center;justify-content:center}

/* hero */
.hero-photo{left:0;top:95px;width:1200px;height:730px;background:linear-gradient(180deg,#5a5e66 0%,#8a6a3a 35%,#b9873f 55%,#6b4a25 80%,#3c2b1a 100%)}
.nav{left:335px;top:74px;width:527px;height:42px;background:var(--nav);display:flex;font-size:12px;color:var(--white);z-index:3}
.nav a{display:flex;align-items:center;padding:0 20px}
.nav a.active{background:var(--blue);padding:0 26px}
.hero-kicker{left:0;width:1200px;top:356px;text-align:center;font-family:"Cinzel",serif;font-weight:700;font-size:19px;color:var(--white)}
.hero-title{left:0;width:1200px;top:380px;text-align:center;font-family:"Cinzel",serif;font-weight:700;font-size:46px;color:var(--white)}
.hero-sub{left:0;width:1200px;top:445px;text-align:center;font-size:12px;color:var(--white)}
.hero-btn{left:538px;top:490px;width:118px;height:37px;border:2px solid var(--white);border-radius:19px;color:var(--white);font-size:12px;display:flex;align-items:center;justify-content:center}
.scroll-mouse{left:585px;top:639px;width:25px;height:50px;border:2px solid var(--white);border-radius:13px}
.scroll-mouse::after{content:"";position:absolute;left:9px;top:10px;width:3px;height:3px;border-radius:50%;background:var(--white)}
.hero-wave{left:0;top:700px;width:1200px;height:130px}

/* about */
.about-title{left:130px;top:886px;font-size:29px}
.about-text{left:130px;top:982px;width:465px;font-size:11px;line-height:22.5px}
.about-photo{left:625px;top:875px;width:441px;height:322px;border-radius:4px;background:linear-gradient(180deg,#4d86d6 0%,#9fc2ea 45%,#e9ecef 60%,#cfd3d6 78%,#4f8f32 88%,#3e7a27 100%)}

/* services */
.section-title{left:0;width:1200px;text-align:center;font-size:29px}
.service{position:absolute;width:300px;text-align:center}
.service-ring{width:222px;height:222px;border-radius:50%;border:2px solid #c8c8c8;margin:0 auto;display:flex;align-items:center;justify-content:center}
.service-name{font-family:"Cinzel",serif;font-weight:600;font-size:17px;color:var(--ink);margin-top:38px}
.service-text{font-size:11px;line-height:18px;margin-top:18px;padding:0 6px}

/* projects */
.project{position:absolute}

/* testimonial */
.testi-photo{left:131px;top:2568px;width:389px;height:283px;border-radius:3px;background:linear-gradient(180deg,#3f7bd0 0%,#9bbde6 35%,#4a5563 52%,#6e7480 62%,#8b8f7a 75%,#5f8d3a 100%)}
.testi-avatar{left:546px;top:2584px;width:104px;height:104px;border-radius:50%;background:radial-gradient(circle at 50% 45%,#c9c1ba,#7c746d)}
.testi-name{left:664px;top:2633px;font-family:"Cinzel",serif;font-weight:700;color:var(--blue);font-size:17px}
.testi-text{left:549px;top:2704px;width:520px;font-size:11px;line-height:22.5px}
.dots{left:553px;top:2825px;display:flex;gap:11px}
.dots span{width:6px;height:6px;border-radius:50%;background:#3d3d3d}
.dots span:first-child{background:var(--blue)}

/* footer */
.footer-wave{left:0;top:2965px;width:1200px;height:200px}
.footer-body{left:0;top:3150px;width:1200px;height:295px;background:var(--footer-blue)}
.foot-brand{left:74px;top:3188px;display:flex;align-items:center;gap:8px}
.foot-brand .brand-mark{background:var(--white)}
.foot-brand .brand-name{color:var(--white)}
.foot-about{left:74px;top:3250px;width:255px;font-size:11px;line-height:18px;color:var(--white)}
.foot-more{left:76px;top:3377px;font-size:11px;color:var(--white);text-decoration:underline}
.foot-title{position:absolute;top:3180px;font-family:"Cinzel",serif;font-weight:700;color:var(--white);font-size:17px}
.foot-links{left:406px;top:3250px;font-size:11px;line-height:16.5px;color:var(--white);list-style:none}
.contact-row{position:absolute;left:571px;display:flex;gap:8px;font-size:11px;line-height:16px;color:var(--white)}
.contact-row svg{flex:none;margin-top:2px}
.field{position:absolute;background:var(--white);border-radius:14px;font-size:10px;color:#b0b0b0;font-style:italic;padding:8px 22px}
.submit{left:806px;top:3357px;width:117px;height:30px;border-radius:15px;background:var(--grey-bar);color:var(--white);font-size:11px;display:flex;align-items:center;justify-content:center}
.bottom-bar{left:0;top:3445px;width:1200px;height:41px;background:var(--grey-bar)}
.copyright{left:74px;top:3458px;font-size:11px;color:var(--white)}
.socials{left:969px;top:3451px;display:flex;gap:15px}
.socials span{width:28px;height:28px;border-radius:50%;border:2px solid var(--white)}
</style>
</head>
<body>

<!-- header -->
<div class="abs call">
  <div class="call-icon">
    <svg width="16" height="16" viewBox="0 0 24 24"><path fill="#fff" d="M6.6 10.8a15.1 15.1 0 0 0 6.6 6.6l2.2-2.2c.3-.3.7-.4 1-.2 1.1.4 2.3.6 3.6.6.6 0 1 .4 1 1V20c0 .6-.4 1-1 1A17 17 0 0 1 3 4c0-.6.4-1 1-1h3.5c.6 0 1 .4 1 1 0 1.3.2 2.5.6 3.6.1.3 0 .7-.2 1z"/></svg>
  </div>
  <div class="call-text">Call us now<br><span>(+00) 123 456 789</span></div>
</div>
<div class="abs brand"><div class="brand-mark"></div><div class="brand-name">Merrivale Construction</div></div>
<a class="abs quote-btn" href="#">Get a Quote</a>

<!-- hero -->
<div class="abs hero-photo" role="img" aria-label="Luxury Mediterranean-style home lit warmly at dusk"></div>
<nav class="abs nav">
  <a class="active" href="#">Home</a><a href="#">About us</a><a href="#">Services</a><a href="#">Gallery</a><a href="#">Testimonial</a><a href="#">Contact us</a>
</nav>
<div class="abs hero-kicker">High End Luxury</div>
<h1 class="abs hero-title">Custom Home Builder</h1>
<p class="abs hero-sub">Lorem Ipsum is simply dummy text of the printing and typesetting industry.</p>
<a class="abs hero-btn" href="#">Contact us</a>
<div class="abs scroll-mouse"></div>
<svg class="abs hero-wave" viewBox="0 0 1200 130" preserveAspectRatio="none">
  <path d="M0 80 C200 20 330 50 520 95 C720 140 900 80 1200 25 L1200 130 L0 130Z" fill="#fff"/>
  <path d="M0 80 C200 20 330 50 520 95 C720 140 900 80 1200 25 L1200 10 C900 70 720 125 520 80 C330 35 200 5 0 70Z" fill="#4a3420"/>
</svg>

<!-- about -->
<h2 class="abs heading about-title">About Us</h2>
<div class="rule" style="left:130px;top:936px;width:145px"></div>
<p class="abs about-text">Lorem Ipsum is simply dummy text of the printing and typesetting industry. Lorem Ipsum has been the industry's standard dummy text ever since the 1500s, when an unknown printer took a galley of type and scrambled it to make a type specimen book. It has survived not only five centuries, but also the leap into electronic typesetting, remaining essentially unchanged.</p>
<a class="btn-outline" href="#" style="left:130px;top:1131px;width:118px;height:37px">Read More</a>
<div class="abs about-photo" role="img" aria-label="White colonial mansion with columns on a green lawn"></div>

<!-- services -->
<h2 class="abs heading section-title" style="top:1283px">Our Services</h2>
<div class="rule" style="left:525px;top:1334px;width:150px"></div>

<div class="service" style="left:123px;top:1380px">
  <div class="service-ring">
    <svg width="96" height="96" viewBox="0 0 96 96" fill="none" stroke="#555" stroke-width="4"><path d="M10 40 L48 12 L86 40"/><rect x="18" y="38" width="60" height="46"/><rect x="38" y="48" width="20" height="16"/><rect x="26" y="52" width="8" height="18"/><rect x="62" y="52" width="8" height="18"/><path d="M10 84 H86 M34 78 H62"/></svg>
  </div>
  <div class="service-name">Custom Homes</div>
  <p class="service-text">Lorem Ipsum is simply dummy text of the printing and typesetting industry. Lorem Ipsum has been the industry's standard dummy text.</p>
  <a class="btn-outline" href="#" style="left:93px;top:386px;width:118px;height:37px">Read More</a>
</div>
<div class="service" style="left:445px;top:1380px">
  <div class="service-ring">
    <svg width="96" height="96" viewBox="0 0 96 96" fill="none" stroke="#555" stroke-width="4"><path d="M8 48 L48 12 L88 48"/><path d="M18 40 V86 H78 V40"/><path d="M64 22 V10 H72 V28" fill="#555"/><path d="M32 44 L66 78 M66 44 L32 78" stroke="#1b6fc0"/></svg>
  </div>
  <div class="service-name">Renovation/Remodeling</div>
  <p class="service-text">Lorem Ipsum is simply dummy text of the printing and typesetting industry. Lorem Ipsum has been the industry's standard dummy text.</p>
  <a class="btn-outline" href="#" style="left:91px;top:386px;width:118px;height:37px">Read More</a>
</div>
<div class="service" style="left:773px;top:1380px">
  <div class="service-ring">
    <svg width="100" height="96" viewBox="0 0 100 96" fill="none" stroke="#555" stroke-width="5"><rect x="8" y="44" width="30" height="16"/><rect x="8" y="60" width="44" height="16"/><rect x="52" y="60" width="40" height="16"/><rect x="30" y="76" width="44" height="14"/><rect x="8" y="76" width="22" height="14"/><rect x="74" y="76" width="18" height="14"/><rect x="38" y="44" width="26" height="16"/><path d="M58 42 L76 24" stroke="#1b6fc0" stroke-width="6"/><circle cx="82" cy="18" r="9" fill="#1b6fc0" stroke="none"/></svg>
  </div>
  <div class="service-name">Additions</div>
  <p class="service-text">Lorem Ipsum is simply dummy text of the printing and typesetting industry. Lorem Ipsum has been the industry's standard dummy text.</p>
  <a class="btn-outline" href="#" style="left:91px;top:386px;width:118px;height:37px">Read More</a>
</div>

<!-- latest projects -->
<h2 class="abs heading section-title" style="top:1964px">Latest Projects</h2>
<div class="rule" style="left:525px;top:2016px;width:150px"></div>
<div class="project" style="left:137px;top:2131px;width:213px;height:150px;background:linear-gradient(160deg,#d8b883,#a57245 60%,#6b4024)" role="img" aria-label="Warm luxury living room interior with arched alcoves"></div>
<div class="project" style="left:357px;top:2073px;width:215px;height:280px;background:linear-gradient(180deg,#1f3a9c 0%,#2c4fb8 40%,#c48a3a 70%,#3a2b1c 100%)" role="img" aria-label="Illuminated home entrance framed by palm trees at night"></div>
<div class="project" style="left:580px;top:2060px;width:226px;height:151px;background:linear-gradient(180deg,#cfd9e1 0%,#e9ecee 45%,#62704c 70%,#8c8f8c 100%)" role="img" aria-label="White estate seen through open entry gates"></div>
<div class="project" style="left:580px;top:2215px;width:226px;height:151px;background:linear-gradient(180deg,#dfe6ec 0%,#f2f2f0 50%,#56743b 80%,#3d5c2a 100%)" role="img" aria-label="White colonial house with chimneys and hedges"></div>
<div class="project" style="left:813px;top:2131px;width:254px;height:177px;background:linear-gradient(180deg,#3b78c9 0%,#8fb5e0 30%,#b26a57 50%,#4f8a3b 70%,#2fa5a8 82%,#5b8f3a 100%)" role="img" aria-label="Aerial view of a red-roofed villa with pool and palms"></div>
<a class="btn-outline" href="#" style="left:525px;top:2412px;width:145px;height:37px">View All Projects</a>

<!-- testimonial -->
<div class="abs testi-photo" role="img" aria-label="Large stone and timber estate home with a wide lawn"></div>
<svg class="abs" style="left:448px;top:2550px" width="54" height="38" viewBox="0 0 54 38"><g fill="none" stroke="#1b6fc0" stroke-width="4"><path d="M22 4 C10 8 4 16 4 26 A8 8 0 1 0 14 18"/><path d="M50 4 C38 8 32 16 32 26 A8 8 0 1 0 42 18"/></g></svg>
<div class="abs testi-avatar" role="img" aria-label="Client portrait"></div>
<div class="abs testi-name">Daniel Hartley</div>
<p class="abs testi-text">Lorem Ipsum is simply dummy text of the printing and typesetting industry. Lorem Ipsum has been the industry's standard dummy text ever since the 1500s, when an unknown printer took a galley of type and scrambled it to make a type specimen book. It has survived not only five centuries, but also the leap into electronic typesetting, remaining essentially unchanged.</p>
<div class="abs dots"><span></span><span></span><span></span><span></span></div>

<!-- footer -->
<svg class="abs footer-wave" viewBox="0 0 1200 200" preserveAspectRatio="none">
  <path d="M0 130 C250 20 450 20 700 95 C900 150 1050 60 1200 10 L1200 200 L0 200Z" fill="#2573b9"/>
  <path d="M0 120 C260 10 460 20 700 85 C900 135 1050 50 1200 0 L1200 30 C1050 80 900 160 700 110 C460 45 260 40 0 150Z" fill="#1a5fa6" opacity="0.6"/>
  <path d="M0 170 C300 90 500 140 760 190 C950 215 1100 160 1200 120 L1200 200 L0 200Z" fill="#2573b9"/>
  <path d="M0 165 C300 85 500 135 760 178" fill="none" stroke="#fff" stroke-width="3"/>
</svg>
<div class="abs footer-body"></div>
<div class="abs foot-brand"><div class="brand-mark"></div><div class="brand-name">Merrivale Construction</div></div>
<p class="abs foot-about">Lorem Ipsum is simply dummy text of the printing and typesetting industry. Lorem Ipsum has been the industry's standard dummy text ever since the 1500s, when an unknown printer took a galley of type and scrambled it to make a type specimen book.</p>
<a class="abs foot-more" href="#">Read More</a>

<div class="foot-title" style="left:406px">Quick Links</div>
<ul class="abs foot-links"><li>Home</li><li>About us</li><li>Services</li><li>Gallery</li><li>Testimonial</li><li>Contact us</li></ul>

<div class="foot-title" style="left:575px">Contact Detail</div>
<div class="contact-row" style="top:3250px">
  <svg width="12" height="12" viewBox="0 0 24 24"><circle cx="12" cy="12" r="12" fill="#fff"/><path fill="#2573b9" d="M8 6l2 3-1 1.5a8 8 0 0 0 4.5 4.5L15 14l3 2-1 2.5C11 18 6 13 5.5 7z"/></svg>
  <div>(+00) 123 456 789<br>(+00) 123 456 789</div>
</div>
<div class="contact-row" style="top:3298px">
  <svg width="12" height="12" viewBox="0 0 24 24"><circle cx="12" cy="12" r="12" fill="#fff"/><rect x="6" y="8" width="12" height="8" fill="none" stroke="#2573b9" stroke-width="2"/></svg>
  <div>info@merrivaleconstruction.com</div>
</div>
<div class="contact-row" style="top:3331px">
  <svg width="12" height="12" viewBox="0 0 24 24"><circle cx="12" cy="12" r="12" fill="#fff"/><path fill="#2573b9" d="M12 5a5 5 0 0 0-5 5c0 4 5 9 5 9s5-5 5-9a5 5 0 0 0-5-5zm0 7a2 2 0 1 1 0-4 2 2 0 0 1 0 4z"/></svg>
  <div>4415 Larkfield Ave.<br>Riverton, NC 28300</div>
</div>

<div class="foot-title" style="left:805px">Contact Us</div>
<div class="field" style="left:805px;top:3214px;width:157px;height:30px">Full Name</div>
<div class="field" style="left:967px;top:3214px;width:156px;height:30px">Email</div>
<div class="field" style="left:805px;top:3251px;width:318px;height:88px">Message</div>
<a class="abs submit" href="#">Submit Now</a>

<div class="abs bottom-bar"></div>
<div class="abs copyright">Copyright © 2020 merrivaleconstruction.All Rights Reserved</div>
<div class="abs socials"><span></span><span></span><span></span><span></span></div>

</body>
</html>
```